Brackenvale.com Postcard

We want to create a postcard, which is going to be mailed out to 6k managers at Hospitals throughout the USA.

I attached a rough draft of what I want the postcard to look like, but want it to look much better. The postcard size is 5.47" * 4.21"

```html
<!DOCTYPE html>
<html lang="en">
<head>
<meta charset="utf-8">
<title>Brackenvale Medical – We Buy IV Pumps Postcard</title>
<link href="https://fonts.googleapis.com/css2?family=Cabin:ital,wght@0,500;1,400&family=Orbitron:wght@800&display=swap" rel="stylesheet">
<style>
  :root {
    --navy: #22387a;
    --navy-deep: #1b2d66;
    --blue: #1f63b8;
    --sky: #bfe0f5;
    --ink-grey: #6a6a6a;
    --paper: #ffffff;
  }
  * { margin: 0; padding: 0; box-sizing: border-box; }
  html, body { width: 1200px; height: 930px; overflow: hidden; background: var(--paper); }
  .postcard { position: relative; width: 1200px; height: 930px; background: var(--paper); overflow: hidden; }
  .edge-artwork {
    position: absolute; left: 0; top: 0; width: 300px; height: 930px;
    background: linear-gradient(90deg, rgba(31,99,184,0.75) 0%, rgba(191,224,245,0.55) 30%, rgba(255,255,255,0) 100%);
  }
  .corner-artwork {
    position: absolute; left: 0; bottom: 0; width: 200px; height: 170px;
    background: radial-gradient(ellipse at 0% 100%, rgba(31,99,184,0.8) 0%, rgba(191,224,245,0.5) 55%, rgba(255,255,255,0) 75%);
  }
  .brand {
    position: absolute; left: 56px; top: 56px;
    display: flex; align-items: center; gap: 10px;
    font-family: "Cabin", sans-serif; font-weight: 500;
    font-variant: small-caps; font-size: 24px; letter-spacing: 0.5px;
    color: var(--navy-deep);
  }
  .brand-dot { width: 22px; height: 22px; border-radius: 50%; background: var(--navy-deep); }
  .contact {
    position: absolute; left: 95px; top: 90px;
    font-family: "Cabin", sans-serif; font-style: italic; font-weight: 400;
    font-size: 24px; line-height: 31.5px; color: var(--ink-grey);
    list-style: none;
  }
  .divider {
    position: absolute; left: 567px; top: 162px;
    width: 2px; height: 588px; background: var(--navy-deep);
  }
  .headline {
    position: absolute; right: 676px; top: 412px;
    font-family: "Orbitron", sans-serif; font-weight: 800;
    font-size: 58px; line-height: 68px; text-align: right;
    color: var(--navy);
    transform: scaleY(1.28); transform-origin: right top;
    text-shadow: 1px 1px 0 #4d63a3, 2px 2px 2px rgba(0,0,0,0.25);
  }
</style>
</head>
<body>
<main class="postcard">
  <div class="edge-artwork" role="img" aria-label="Decorative blue sweeping band artwork along the left edge"></div>
  <div class="corner-artwork" role="img" aria-label="Decorative blue sweeping band artwork in the lower left corner"></div>

  <div class="brand"><span class="brand-dot"></span><span class="brand-name">Brackenvale Medical</span></div>

  <ul class="contact">
    <li>Po Box 318</li>
    <li>Fernbrook, NC 27999</li>
    <li>555-014-2370</li>
    <li>sales@Brackenvale.com</li>
    <li>Brackenvale.com</li>
  </ul>

  <h1 class="headline">WE BUY<br>IV PUMPS</h1>

  <div class="divider"></div>
</main>
</body>
</html>
```